Business Cards and Stationary for Physio
Brookvale Phsyiotherapy Clinic
Business Cards and Stationary for Physio -
Creative Brief
Simple
First Last
Physiotherapist B. Physio
Street Name, City, Zip
info@brookvalephysiotherapy.example
www.brookvalephysiotherapy.example
Brookvale Phsyiotherapy Clinic. Next Appointment Date Time

```html
<!DOCTYPE html>
<html lang="en">
<head>
<meta charset="utf-8">
<title>Brookvale Phsyiotherapy Clinic – Stationery</title>
<link href="https://fonts.googleapis.com/css2?family=Open+Sans:wght@400;600&display=swap" rel="stylesheet">
<style>
:root{
  --stage:#e8e5e1;
  --paper:#ffffff;
  --blue:#2b3c8f;
  --green:#7ab532;
  --ink:#555a63;
  --soft:#8a8f97;
  --shadow:0 2px 6px rgba(0,0,0,.18);
}
*{margin:0;padding:0;box-sizing:border-box}
html,body{width:1200px;height:897px;overflow:hidden}
body{background:var(--stage);font-family:"Open Sans",sans-serif;color:var(--ink);position:relative}
.sheet{position:absolute;background:var(--paper);box-shadow:var(--shadow);overflow:hidden}
.brand{display:flex;align-items:center;gap:4px;color:var(--blue);font-weight:600;line-height:1.05}
.brand .dot{width:9px;height:9px;border-radius:50%;background:var(--green);flex:none}
.brand .name{font-size:10px}
.brand .name small{display:block;font-size:5px;letter-spacing:.3px}

/* letterheads */
.letter{width:316px;height:460px;padding:22px 26px}
.letter-one{left:63px;top:68px}
.letter-two{left:402px;top:68px}
.letter .contact{position:absolute;right:26px;top:24px;font-size:4.6px;line-height:1.45;color:var(--soft)}
.letter .contact strong{color:var(--blue);font-weight:600}
.letter .body{margin-top:42px;font-size:4.6px;line-height:1.55;color:var(--soft)}
.letter .body p{margin-bottom:6px}
.letter .addr{margin-bottom:10px}
.letter .site{position:absolute;left:26px;bottom:14px;font-size:5px;color:var(--blue);font-weight:600}
.band{position:absolute;left:0;right:0;bottom:0}
.band .g{height:2px;background:var(--green)}
.band .b{height:7px;background:var(--blue)}

/* envelopes */
.envelope{width:318px;height:140px;padding:14px 16px}
.env-one{left:63px;top:589px}
.env-two{left:417px;top:589px}
.envelope .return{margin-top:6px;font-size:4.6px;line-height:1.45;color:var(--soft)}

/* cards */
.card{width:196px;height:114px;border-radius:6px;padding:14px 14px}
.card-a{left:739px;top:145px}
.card-b{left:953px;top:145px}
.card-c{left:739px;top:279px}
.card-d{left:953px;top:279px}
.card-appt{left:848px;top:410px;height:112px}
.card .person{position:absolute;right:14px;top:16px;text-align:right;font-size:6px;color:var(--blue);font-weight:600;line-height:1.4}
.card .person span{display:block;font-size:4.6px;color:var(--soft);font-weight:400}
.card .details{margin-top:12px;font-size:4.6px;line-height:1.45;color:var(--soft)}
.card .band .b{height:6px}
.appt-title{margin-top:8px;font-size:5.5px;color:var(--blue);font-weight:600}
.slots{display:flex;justify-content:space-between;margin-top:6px;padding:0 6px}
.slot{width:20px;text-align:center;font-size:4px;color:var(--soft)}
.slot i{display:block;height:12px;border:1px solid var(--green);border-radius:2px;margin-bottom:2px}
.appt-site{position:absolute;left:0;right:0;bottom:6px;text-align:center;font-size:4.6px;color:var(--blue)}
</style>
</head>
<body>

<section class="sheet letter letter-one">
  <div class="brand"><span class="dot"></span><span class="name">Brookvale<small>PHSYIOTHERAPY CLINIC</small></span></div>
  <div class="contact"><strong>Address</strong><br>Street Name, City, Zip<br>Ph 0400 000 000<br>Fax 0400 000 001<br>info@brookvalephysiotherapy.example</div>
  <div class="body">
    <p class="addr">Mr Sample Patient<br>12 Example Road<br>Suburb State 0000</p>
    <p>1 January 2024</p>
    <p>Dear Mr Patient,</p>
    <p>Thank you for choosing our clinic for your recent treatment. We are pleased to confirm your care plan and the exercises we discussed during your visit. Please keep this letter with your records and bring it to your next session.</p>
    <p>Your program focuses on restoring strength, balance and range of motion. Each visit builds on the last, so steady attendance matters. If you feel any new pain between sessions, please call us before your next booked time.</p>
    <p>We also offer hydrotherapy, sports injury care and clinical pilates classes for all ages. Ask at reception about group times, pricing and rebates that may apply to your health fund cover.</p>
    <p>Thank you again for your trust. We look forward to helping you move well and feel better.</p>
    <p>Kind regards,<br><br>First Last<br>Physiotherapist B. Physio</p>
  </div>
  <div class="site">www.brookvalephysiotherapy.example</div>
</section>

<section class="sheet letter letter-two">
  <div class="brand"><span class="dot"></span><span class="name">Brookvale<small>PHSYIOTHERAPY CLINIC</small></span></div>
  <div class="contact"><strong>Address</strong><br>Street Name, City, Zip<br>Ph 0400 000 000<br>Fax 0400 000 001<br>info@brookvalephysiotherapy.example</div>
  <div class="body">
    <p class="addr">Mr Sample Patient<br>12 Example Road<br>Suburb State 0000</p>
    <p>1 January 2024</p>
    <p>Dear Mr Patient,</p>
    <p>Thank you for choosing our clinic for your recent treatment. We are pleased to confirm your care plan and the exercises we discussed during your visit. Please keep this letter with your records and bring it to your next session.</p>
    <p>Your program focuses on restoring strength, balance and range of motion. Each visit builds on the last, so steady attendance matters. If you feel any new pain between sessions, please call us before your next booked time.</p>
    <p>We also offer hydrotherapy, sports injury care and clinical pilates classes for all ages. Ask at reception about group times, pricing and rebates that may apply to your health fund cover.</p>
    <p>Thank you again for your trust. We look forward to helping you move well and feel better.</p>
    <p>Kind regards,<br><br>First Last<br>Physiotherapist B. Physio</p>
  </div>
  <div class="band"><div class="g"></div><div class="b"></div></div>
</section>

<section class="sheet envelope env-one">
  <div class="brand"><span class="dot"></span><span class="name">Brookvale<small>PHSYIOTHERAPY CLINIC</small></span></div>
  <div class="return">Street Name, City, Zip</div>
</section>

<section class="sheet envelope env-two">
  <div class="brand"><span class="dot"></span><span class="name">Brookvale<small>PHSYIOTHERAPY CLINIC</small></span></div>
  <div class="return">Street Name, City, Zip</div>
  <div class="band"><div class="g"></div><div class="b"></div></div>
</section>

<section class="sheet card card-a">
  <div class="brand"><span class="dot"></span><span class="name">Brookvale<small>PHSYIOTHERAPY CLINIC</small></span></div>
  <div class="person">First Last<span>Physiotherapist B. Physio</span></div>
  <div class="details">Street Name, City, Zip<br>Ph 0400 000 000<br>info@brookvalephysiotherapy.example</div>
</section>

<section class="sheet card card-b">
  <div class="brand"><span class="dot"></span><span class="name">Brookvale<small>PHSYIOTHERAPY CLINIC</small></span></div>
  <div class="person">First Last<span>Physiotherapist B. Physio</span></div>
  <div class="details">Street Name, City, Zip<br>Ph 0400 000 000<br>info@brookvalephysiotherapy.example</div>
  <div class="band"><div class="g"></div><div class="b"></div></div>
</section>

<section class="sheet card card-c">
  <div class="brand"><span class="dot"></span><span class="name">Brookvale<small>PHSYIOTHERAPY CLINIC</small></span></div>
  <div class="person">First Last<span>Physiotherapist B. Physio</span></div>
  <div class="details">Street Name, City, Zip<br>Ph 0400 000 000<br>info@brookvalephysiotherapy.example</div>
</section>

<section class="sheet card card-d">
  <div class="brand"><span class="dot"></span><span class="name">Brookvale<small>PHSYIOTHERAPY CLINIC</small></span></div>
  <div class="person">First Last<span>Physiotherapist B. Physio</span></div>
  <div class="details">Street Name, City, Zip<br>Ph 0400 000 000<br>info@brookvalephysiotherapy.example</div>
  <div class="band"><div class="g"></div><div class="b"></div></div>
</section>

<section class="sheet card card-appt">
  <div class="brand"><span class="dot"></span><span class="name">Brookvale<small>PHSYIOTHERAPY CLINIC</small></span></div>
  <div class="appt-title">Next Appointment</div>
  <div class="slots">
    <div class="slot"><i></i>Date</div>
    <div class="slot"><i></i>Time</div>
    <div class="slot"><i></i>Date</div>
    <div class="slot"><i></i>Time</div>
    <div class="slot"><i></i>Date</div>
    <div class="slot"><i></i>Time</div>
  </div>
  <div class="appt-site">www.brookvalephysiotherapy.example</div>
</section>

</body>
</html>
```